Broschüre KTR Festival
Zielgruppe
Wir sind ein Verband, der Ensembles der Amateurmusik (Blasorchester, Chöre, Akkordeonensembles ....) vertritt. Unsere Zielgruppe sind Menschen, die in ihrer Freizeit musizieren ebenso, wie Menschen die gerne Konzerte besuchen.
Die Broschüre ist ein Programmheft für ein eintägiges Festival mit mehreren Open-Air Bühnen.
Aufgabenstellung
Die Broschüre sollte DIN lang Format sein, damit sie gut in die Westentasche passt. Zentraler Bestandteil neben den Textseiten sind die Termintabellen, die die Auftritte auf den Bühnen abbilden.

```html
<!DOCTYPE html>
<html lang="en">
<head>
<meta charset="utf-8">
<title>KTR Festival – Programm</title>
<link href="https://fonts.googleapis.com/css2?family=Oswald:wght@200;300;600&family=Open+Sans:wght@400;600;700&family=Cabin:wght@600&display=swap" rel="stylesheet">
<style>
  :root {
    --bg: #dcdcdc;
    --teal: #1f9281;
    --teal-soft: #5fb3a6;
    --paper: #ffffff;
    --text: #555555;
    --brown: #8a7a6c;
    --stripe-1: #1f9281;
    --stripe-2: #2d5fa8;
    --stripe-3: #d6334a;
    --stripe-4: #f2a23a;
    --photo-stage: #6f7a80;
    --photo-brass: #8a7256;
  }
  * { box-sizing: border-box; margin: 0; padding: 0; }
  html, body { width: 1200px; height: 750px; overflow: hidden; background: var(--bg); }
  body { display: flex; align-items: center; justify-content: center; font-family: "Open Sans", sans-serif; }

  .brochure { display: grid; grid-template-columns: repeat(4, 280px); height: 600px; box-shadow: 0 10px 30px rgba(0,0,0,.18); }
  .panel { position: relative; height: 100%; overflow: hidden; display: flex; flex-direction: column; }
  .panel--white { background: var(--paper); padding: 14px 12px 0; }
  .panel--teal { background: var(--teal); color: #fff; }

  .stripes { height: 8px; background: linear-gradient(var(--stripe-1) 0 25%, var(--stripe-2) 25% 50%, var(--stripe-3) 50% 75%, var(--stripe-4) 75% 100%); }
  .stripes--top { position: absolute; top: 0; left: 0; right: 0; }
  .stripes--bottom { position: absolute; bottom: 0; left: 0; right: 0; }

  .photo { height: 150px; margin-top: 6px; }
  .photo--brass { background: linear-gradient(135deg, var(--photo-brass), #c9b48a 60%, #5a6670); }
  .photo--choir { background: linear-gradient(180deg, #3c4146, var(--photo-stage) 45%, #e6e6e6 75%, #8b9a6c); }

  .artist { text-align: right; padding: 10px 4px 8px; }
  .artist__name { font-family: "Cabin", sans-serif; font-size: 14px; color: var(--teal); }
  .artist__name span { color: var(--brown); }
  .artist__theme { font-size: 7px; font-weight: 700; color: var(--teal); text-transform: uppercase; margin: 2px 0 6px; }
  .artist__theme span { color: var(--brown); }
  .artist__text { font-size: 7.5px; line-height: 1.75; color: var(--text); text-align: center; }

  .url-line { position: absolute; bottom: 12px; left: 0; right: 0; font-size: 6.5px; letter-spacing: .5px; color: var(--teal); white-space: nowrap; text-align: center; }
  .panel--teal .url-line { color: #d7efeb; }

  .ornament { position: absolute; top: 70px; width: 90px; height: 380px; background: var(--teal-soft); opacity: .55; border-radius: 45px; }
  .ornament--left { left: 10px; }
  .ornament--right { right: 10px; }

  .program { position: relative; padding: 36px 18px 0 110px; text-align: right; }
  .program--right { padding: 30px 110px 0 18px; text-align: left; }
  .program__title { font-family: "Oswald", sans-serif; font-size: 24px; font-weight: 200; letter-spacing: -.5px; }
  .program__title strong { font-weight: 600; }
  .program__intro { font-size: 7.5px; line-height: 1.9; margin: 12px 0 8px; }

  .slot { padding: 8px 0 10px; border-bottom: 1px dotted rgba(255,255,255,.5); }
  .slot:last-child { border-bottom: 0; }
  .slot__time { font-family: "Oswald", sans-serif; font-weight: 200; font-size: 24px; line-height: 1; letter-spacing: -1px; }
  .slot__title { font-family: "Cabin", sans-serif; font-size: 12.5px; margin-top: 3px; }
  .slot__theme { font-size: 6.5px; font-weight: 700; text-transform: uppercase; }
  .slot__place { font-size: 5.5px; text-transform: uppercase; opacity: .85; }
  .program--left-list { margin-left: -80px; }
  .program--left-list .slot { padding-left: 0; }

  .tickets { margin-top: 6px; }
  .tickets__title { font-family: "Cabin", sans-serif; font-size: 15px; }
  .tickets__phone { font-size: 11px; font-weight: 600; margin-top: 4px; }
  .tickets__mail { font-size: 7px; font-weight: 700; }
</style>
</head>
<body>
<main class="brochure">

  <section class="panel panel--white">
    <div class="stripes stripes--top"></div>
    <div class="photo photo--brass" role="img" aria-label="Photo of a wind orchestra playing outdoors"></div>
    <article class="artist">
      <h3 class="artist__name">Artist or Band <span>Name</span></h3>
      <p class="artist__theme">Title of the theme - <span>Music start h 10.00</span></p>
      <p class="artist__text">Lorem ipsum dolor sit amet, consectetur adipiscing elit, sed do eiusmod tempor incididunt ut labore et dolore magna aliqua. Ut enim ad minim veniam, quis nostrud exercitation ullamco laboris nisi ut aliquip ex ea commodo consequat.</p>
    </article>
    <div class="photo photo--choir" role="img" aria-label="Photo of a choir on an open-air stage with a conductor"></div>
    <article class="artist">
      <h3 class="artist__name">Artist or Band <span>Name</span></h3>
      <p class="artist__theme">Title of the theme - <span>Music start h 10.00</span></p>
      <p class="artist__text">Lorem ipsum dolor sit amet, consectetur adipiscing elit, sed do eiusmod tempor incididunt ut labore et dolore magna aliqua. Ut enim ad minim veniam, quis nostrud exercitation ullamco laboris nisi ut aliquip ex ea commodo consequat.</p>
    </article>
    <p class="url-line">www.ktr-musikfest.de - www.ktr-musikfest.de - www.ktr-musikfest.de</p>
    <div class="stripes stripes--bottom"></div>
  </section>

  <section class="panel panel--teal">
    <div class="ornament ornament--left" role="img" aria-label="Decorative white music-note ornament"></div>
    <div class="program">
      <h2 class="program__title">FESTIVAL <strong>PROGRAM</strong></h2>
      <p class="program__intro">Lorem ipsum dolor sit amet, consectetur adipiscing elit, sed do eiusmod tempor incididunt ut labore et dolore magna aliqua. Ut enim ad minim veniam, quis nostrud exercitation ullamco laboris nisi ut aliquip ex ea commodo consequat.</p>
      <div class="program--left-list">
        <div class="slot"><p class="slot__time">09.30</p><p class="slot__title">Eventi Title</p><p class="slot__theme">Festival press conference</p><p class="slot__place">Location goes here</p></div>
        <div class="slot"><p class="slot__time">11.30</p><p class="slot__title">Eventi Title</p><p class="slot__theme">Concert theme number 1</p><p class="slot__place">Location goes here</p></div>
        <div class="slot"><p class="slot__time">11.30</p><p class="slot__title">Eventi Title</p><p class="slot__theme">Concert theme number 2</p><p class="slot__place">Location goes here</p></div>
        <div class="slot"><p class="slot__time">12.00</p><p class="slot__title">Eventi Title</p><p class="slot__theme">Concert theme number 3</p><p class="slot__place">Location goes here</p></div>
      </div>
    </div>
    <p class="url-line">www.ktr-musikfest.de - www.ktr-musikfest.de</p>
    <div class="stripes stripes--bottom"></div>
  </section>

  <section class="panel panel--teal">
    <div class="ornament ornament--right" role="img" aria-label="Decorative white music-note ornament"></div>
    <div class="program program--right">
      <div class="slot"><p class="slot__time">13.30</p><p class="slot__title">Eventi Title</p><p class="slot__theme">Concert theme number 4</p><p class="slot__place">Location goes here</p></div>
      <div class="slot"><p class="slot__time">14.30</p><p class="slot__title">Eventi Title</p><p class="slot__theme">Concert theme number 5</p><p class="slot__place">Location goes here</p></div>
      <div class="slot"><p class="slot__time">16.30</p><p class="slot__title">Eventi Title</p><p class="slot__theme">Concert theme number 6</p><p class="slot__place">Location goes here</p></div>
      <div class="slot"><p class="slot__time">19.30</p><p class="slot__title">Eventi Title</p><p class="slot__theme">Concert theme number 7</p><p class="slot__place">Location goes here</p></div>
      <div class="slot"><p class="slot__time">22.30</p><p class="slot__title">Eventi Title</p><p class="slot__theme">Concert theme number 8</p><p class="slot__place">Location goes here</p></div>
      <div class="tickets">
        <h3 class="tickets__title">Info and Tickets</h3>
        <p class="tickets__phone">+49 00 11 22 33 789</p>
        <p class="tickets__mail">tickets@ktr-musikfest.de</p>
      </div>
    </div>
    <p class="url-line">www.ktr-musikfest.de - www.ktr-musikfest.de</p>
    <div class="stripes stripes--bottom"></div>
  </section>

  <section class="panel panel--white">
    <div class="stripes stripes--top"></div>
    <div class="photo photo--choir" role="img" aria-label="Photo of a choir on an open-air stage with a conductor"></div>
    <article class="artist">
      <h3 class="artist__name">Artist or Band <span>Name</span></h3>
      <p class="artist__theme">Title of the theme - <span>Music start h 10.00</span></p>
      <p class="artist__text">Lorem ipsum dolor sit amet, consectetur adipiscing elit, sed do eiusmod tempor incididunt ut labore et dolore magna aliqua. Ut enim ad minim veniam, quis nostrud exercitation ullamco laboris nisi ut aliquip ex ea commodo consequat.</p>
    </article>
    <div class="photo photo--brass" role="img" aria-label="Photo of a wind orchestra playing outdoors"></div>
    <article class="artist">
      <h3 class="artist__name">Artist or Band <span>Name</span></h3>
      <p class="artist__theme">Title of the theme - <span>Music start h 10.00</span></p>
      <p class="artist__text">Lorem ipsum dolor sit amet, consectetur adipiscing elit, sed do eiusmod tempor incididunt ut labore et dolore magna aliqua. Ut enim ad minim veniam, quis nostrud exercitation ullamco laboris nisi ut aliquip ex ea commodo consequat.</p>
    </article>
    <p class="url-line">www.ktr-musikfest.de - www.ktr-musikfest.de - www.ktr-musikfest.de</p>
    <div class="stripes stripes--bottom"></div>
  </section>

</main>
</body>
</html>
```